Brixel Forge
Stationary for a S/W company
Brixel Forge -
Creative Brief
Use specific fonts
Dinesh Varma
Chief Operating Officer
14587 Harrow Court Brambleton, VA 20148
(800) 555 4bxf
(800) 555 2bxf
dinesh.varma@brixelforge.example
www.brixelforge.example
Front side: Dinesh Varma Chief Operating Officer t (703) 555 0147 dinesh.varma@brixelforge.example Back Side: www.brixelforge.example 14587 Harrow Court Brambleton, VA 20148 Toll free: t (800) 555 4bxf, f (800) 555 2bxf The key word is "CLEAN" and "Unique". If watermark, it should be really light. Normal edges. Pick the fonts and colors of your choice that will go with the logo. You can always try to keep all information on front but I want to keep the front of the business card as clean as possible with all "most used" information. The logo should be of focus. Same rule applies to letter head and envelopes. Also, need design for "thank you" cards and brochure. Good luck.
www.brixelforge.example 14587 Harrow Court, Brambleton, VA 20148 Toll free: t (800) 555 4bxf, f (800) 555 2bxf

```html
<!DOCTYPE html>
<html lang="en">
<head>
<meta charset="utf-8">
<title>Brixel Forge Stationery</title>
<link href="https://fonts.googleapis.com/css2?family=Montserrat:wght@600&family=Open+Sans:wght@400;600&display=swap" rel="stylesheet">
<style>
  :root {
    --navy: #1b2f7a;
    --blue-deep: #0e2a80;
    --blue-mid: #2a5fb8;
    --blue-light: #4f8fd8;
    --sky: #9cc3ea;
    --gold: #e2a526;
    --ink: #222;
    --grey: #8a8f99;
    --rule: #b9bec8;
    --paper: #ffffff;
    --frame: #c9ccd2;
  }
  html, body { margin: 0; padding: 0; }
  body {
    width: 1200px; height: 901px; overflow: hidden;
    background: var(--paper); position: relative;
    font-family: "Open Sans", Arial, sans-serif; color: var(--ink);
  }
  .label {
    position: absolute; font-size: 17px; color: var(--ink);
    transform: translateX(-50%); white-space: nowrap;
  }
  .envelope {
    position: absolute; left: 29px; top: 58px; width: 1142px; height: 497px;
    border: 1px solid var(--frame); box-sizing: border-box; background: var(--paper);
    overflow: hidden;
  }
  .envelope__band {
    position: absolute; left: 0; top: 0; right: 0; height: 22px;
    background: linear-gradient(90deg, #eaf2fb 0%, var(--sky) 35%, var(--blue-mid) 75%, var(--blue-deep) 100%);
  }
  .brand__dot { position: absolute; border-radius: 50%; background: var(--gold); }
  .brand__name {
    position: absolute; font-family: "Montserrat", Arial, sans-serif; font-weight: 600;
    color: var(--navy); white-space: nowrap; line-height: 1;
  }
  .divider { position: absolute; width: 1px; background: var(--rule); }
  .small {
    position: absolute; color: var(--grey); line-height: 1.35; white-space: nowrap;
  }
  .envelope__mark {
    position: absolute; right: 20px; bottom: 6px; width: 225px; height: 225px;
    border-radius: 50%; background: #eef3fa;
  }
  .card {
    position: absolute; width: 421px; height: 242px; box-sizing: border-box;
    overflow: hidden;
  }
  .card--front { left: 160px; top: 624px; border: 1px solid var(--frame); background: var(--paper); }
  .card--back {
    left: 624px; top: 624px;
    background: linear-gradient(135deg, var(--blue-light) 0%, var(--blue-mid) 35%, var(--blue-deep) 100%);
  }
  .card__mark {
    position: absolute; left: -60px; top: -70px; width: 220px; height: 220px;
    border-radius: 50%; background: rgba(255,255,255,0.12);
  }
  .card__url { position: absolute; left: 22px; bottom: 18px; color: #fff; font-size: 11px; }
  .card__address {
    position: absolute; right: 20px; bottom: 14px; text-align: right;
    color: #dfe8f7; font-size: 8.5px; line-height: 1.3;
  }
  .person__name { font-size: 13px; color: #555; }
  .person__title { font-size: 10px; color: var(--grey); }
</style>
</head>
<body>
  <div class="label" style="left:600px; top:16px;">Envelop #10</div>

  <section class="envelope" aria-label="Number 10 envelope">
    <div class="envelope__band"></div>
    <span class="brand__dot" style="left:120px; top:44px; width:42px; height:42px;"></span>
    <span class="brand__name" style="left:44px; top:134px; font-size:28px;">Brixel Forge</span>
    <div class="divider" style="left:258px; top:128px; height:40px;"></div>
    <div class="small" style="left:268px; top:131px; font-size:11px;">
      14587 Harrow Court<br>Larkhaven, VA 20199
    </div>
    <div class="envelope__mark" role="img" aria-label="Faint brand watermark"></div>
  </section>

  <div class="label" style="left:370px; top:590px;">Front</div>
  <div class="label" style="left:834px; top:598px;">Back</div>

  <section class="card card--front" aria-label="Business card front">
    <span class="brand__dot" style="left:88px; top:126px; width:24px; height:24px;"></span>
    <span class="brand__name" style="left:48px; top:178px; font-size:21px;">Brixel Forge</span>
    <div class="divider" style="left:226px; top:146px; height:66px;"></div>
    <div class="small" style="left:236px; top:146px;">
      <div class="person__name">Dinesh Varma</div>
      <div class="person__title">Chief Operating Officer</div>
      <div style="font-size:8px; margin-top:8px;">t (703) 555 0147</div>
      <div style="font-size:8px;">dinesh.varma@brixelforge.example</div>
    </div>
  </section>

  <section class="card card--back" aria-label="Business card back">
    <div class="card__mark" role="img" aria-label="Large light brand mark"></div>
    <div class="card__url">www.brixelforge.example</div>
    <div class="card__address">
      14587 Harrow Court<br>
      Larkhaven, VA 20199<br>
      Toll free: (800) 555 4bxf<br>
      Fax (800) 555 2bxf
    </div>
  </section>
</body>
</html>
```